Book Cover Design | Science & Nature

We are looking for a cover design for our new educational book titled "Moths Beyond the Hedge".
The full title on the cover can either only be "Moths Beyond the Hedge" or "Garden Moths Beyond the Hedge - a pocket handbook". Up to you what looks good. If the latter, the words "Moths Beyond the Hedge" should be written in larger letters.
The book has a lot information about spiders in general and provides a convenient and understandable identification guide about spiders in California.
The target audience are normal, non-scientist readers who would like to get a simple guide that helps them identify common spiders they will find inside their homes and gardens.
The book is written in an understandable, non-scientific language and contains numerous illustrations and identification sheets of all common spiders.
We are fairly open to suggestions about the design. It should not be too plain as it is not a classic boring science book, but aimed at the average reader. Readers are both male and female, aged 30 and above.
If you know nothing about spiders but would like to know what the spiders in your backyard are, which ones are dangerous and if you want to learn more about spiders, this should be the book you will want to buy!
The author is Dale Prowse. In addition to the author, the book cover should show "Brindlewing.com" - The author can be at the bottom and the website on the top or vice versa.
The cover size is 6" x 9" (15.24 x 22.86 cm). The book has around 150 pages. The back of the book should have a placeholder for the barcode as well as some text. It should also have a quick overview of the main benefits of the book: Easily understandable for non-scientist readers, helpful illustrations, tips on how to deal with spiders in the house and with spider bites. We will obviously add the text later.
I've attached a few of the illustrations as I think they could be used to already give the reader a feeling what they will get with the book. If you think a stock photo will work better than the illustrations, that is fine too.

Target Market(s)

Average readers in the United States wanting to learn more about spiders

Industry/Entity Type

Science, Nature, Spiders, Animals, Education

Requirements
Must have
• When the artwork is generated, the files we would like to receive are: The original working file PSD (Photoshop Document - so any text and images can be edited) All the working elements including: illustrations, photos, graphics and fonts A high resolution (300 dpi), 8.5 x 11 (o- Once r larger) file A JPG file in the exact size specifications and color required by our publisher A JPG file in the exact size for online POD or ebook (Pagelume requires 900x600 ) A JPG black and white (gray scale) variation
Nice to have
• A text (overlay?) could point out some of the advantages of this book: Illustrations and identification guides for all common California spiders, tips on how to get rid of spiders from inside the house, tips on how to deal with arachnophobia, etc. This is optional. Maybe something like "An easy to understand identification guide with plenty of tips and illustrations".
Should not have
• Very dark colors or very feminine colors or shapes.

```html
<!DOCTYPE html>
<html lang="en">
<head>
<meta charset="utf-8">
<title>Moths Beyond the Hedge — Dale Prowse</title>
<link rel="stylesheet" href="https://fonts.googleapis.com/css2?family=Archivo+Black&family=Archivo:wght@400;500;700&display=swap">
<style>
  :root {
    --cover-red: #b5132f;
    --paper: #ffffff;
    --ink-white: #ffffff;
    --site-brown: #4a3b22;
    --spine-ink: #3a2f20;
    --title-shadow: rgba(70, 0, 12, 0.65);
  }
  * { margin: 0; padding: 0; box-sizing: border-box; }
  html, body { width: 794px; height: 1200px; overflow: hidden; background: var(--paper); }
  .cover {
    position: relative;
    width: 794px;
    height: 1200px;
    overflow: hidden;
    background: var(--paper);
    font-family: "Archivo", Arial, sans-serif;
  }

  /* left white column */
  .spine-line {
    position: absolute;
    left: -26px;
    top: 600px;
    transform: translate(0, -50%) rotate(-90deg);
    transform-origin: left top;
    white-space: nowrap;
    font-family: "Archivo Black", Arial, sans-serif;
    font-size: 38px;
    letter-spacing: 6px;
    color: var(--spine-ink);
    width: 1200px;
    text-align: center;
    margin-left: -600px;
  }
  .specimen {
    position: absolute;
    border-radius: 50% 0 0 50%;
  }
  .specimen--orb { left: 185px; top: 22px; width: 102px; height: 265px;
    background: radial-gradient(ellipse at 90% 50%, #6b4a34 0 30%, rgba(140,100,70,.35) 55%, rgba(255,255,255,0) 75%); }
  .specimen--spiny { left: 213px; top: 300px; width: 74px; height: 125px;
    background: radial-gradient(ellipse at 90% 50%, #e8e2d8 0 25%, #1b1b1b 45%, rgba(255,255,255,0) 72%); }
  .specimen--crab { left: 150px; top: 420px; width: 137px; height: 165px;
    background: radial-gradient(ellipse at 95% 60%, #f2e81c 0 35%, rgba(240,225,40,.45) 55%, rgba(255,255,255,0) 75%); }
  .specimen--widow { left: 168px; top: 580px; width: 119px; height: 240px;
    background: radial-gradient(ellipse at 95% 70%, #141010 0 28%, rgba(40,30,30,.4) 52%, rgba(255,255,255,0) 74%); }
  .specimen--wolf { left: 178px; top: 845px; width: 109px; height: 265px;
    background: radial-gradient(ellipse at 95% 55%, #8d7155 0 28%, rgba(180,150,115,.4) 52%, rgba(255,255,255,0) 74%); }

  .website {
    position: absolute;
    left: 44px;
    top: 1141px;
    font-size: 27px;
    letter-spacing: 3.2px;
    color: var(--site-brown);
  }

  /* red panel */
  .panel {
    position: absolute;
    left: 287px;
    top: 0;
    width: 507px;
    height: 1200px;
    background: var(--cover-red);
    color: var(--ink-white);
  }
  .author {
    position: absolute;
    left: 24px;
    top: 124px;
    font-family: "Archivo Black", Arial, sans-serif;
    font-size: 56px;
    letter-spacing: 8px;
    line-height: 1;
    white-space: nowrap;
    text-shadow: 3px 3px 3px var(--title-shadow);
  }
  .title {
    position: absolute;
    left: 22px;
    top: 660px;
    width: 450px;
    font-family: "Archivo Black", Arial, sans-serif;
    text-align: center;
    text-shadow: 4px 4px 4px var(--title-shadow);
  }
  .title__big { display: block; font-size: 108px; line-height: 0.98; letter-spacing: -1px; }
  .title__small { display: block; font-size: 30px; line-height: 1; margin: -4px 0 -6px 0; }

  .tagline {
    position: absolute;
    left: 24px;
    top: 918px;
    width: 470px;
  }
  .tagline__lead {
    font-size: 39px;
    font-weight: 500;
    letter-spacing: 4.6px;
    line-height: 1;
    white-space: nowrap;
  }
  .tagline__sub {
    font-size: 33px;
    font-weight: 700;
    letter-spacing: 3.2px;
    line-height: 1;
    margin-top: 4px;
    white-space: nowrap;
  }
  .tagline__body {
    margin-top: 6px;
    font-size: 19px;
    letter-spacing: 2.3px;
    line-height: 25.8px;
  }
  .tagline__close {
    font-size: 23.5px;
    letter-spacing: 2.6px;
    margin-top: 4px;
    white-space: nowrap;
  }
</style>
</head>
<body>
<main class="cover">
  <div class="spine-line">Garden Moths Beyond the Hedge - a pocket handbook</div>

  <div class="specimen specimen--orb" role="img" aria-label="Illustration of a brown orb-weaver with patterned abdomen"></div>
  <div class="specimen specimen--spiny" role="img" aria-label="Illustration of a black and white spiny orb-weaver"></div>
  <div class="specimen specimen--crab" role="img" aria-label="Illustration of a yellow crab spider"></div>
  <div class="specimen specimen--widow" role="img" aria-label="Illustration of a black widow with red markings"></div>
  <div class="specimen specimen--wolf" role="img" aria-label="Illustration of a tan wolf spider"></div>

  <div class="website">Brindlewing.com</div>

  <section class="panel">
    <div class="author">Dale Prowse</div>

    <h1 class="title">
      <span class="title__big">Moths</span>
      <span class="title__small">beyond the</span>
      <span class="title__big">Hedge</span>
    </h1>

    <div class="tagline">
      <p class="tagline__lead">The Book You Need</p>
      <p class="tagline__sub">for common Knowledge</p>
      <p class="tagline__body">If you know nothing about spiders<br>but would like to know what the spiders<br>in your backyard are, which ones are<br>dangerous and if you want to learn<br>more about spiders,this should be</p>
      <p class="tagline__close">the book you will want to buy!</p>
    </div>
  </section>
</main>
</body>
</html>
```